Create a Powerpoint presentation pack with our new logo

We have just selected a new logo using PixelGuild and we were wanting to create a new Powerpoint presentation pack using this logo.
We'd like the powerpoint pack to have a title page + a header and footer page.
We would like the logo to appear on the title page and the header / footer page.
We are flexible with colours and want something that reflects an IT / travel flair.

I have attached the logo that we just selected from the pixelguild page.

Larkmoor Systems Division is the IT division of Larkmoor Voyage Holdings which is the largest travel retailer in Australia. We have offices in the US, Canada, UK, Singapore, Hong Kong, UAE, India, South Africa, Mexico and New Zealand.

```html
<!DOCTYPE html>
<html lang="en">
<head>
<meta charset="utf-8">
<title>Larkmoor Systems Division – Presentation Pack</title>
<link href="https://fonts.googleapis.com/css2?family=Montserrat:wght@400;600;700&family=Raleway:wght@300;400;600&display=swap" rel="stylesheet">
<style>
:root{
  --red:#e8222c;
  --ink:#161616;
  --stone:#807b78;
  --stone-light:#c9c6c4;
  --mist:#eceaea;
  --text:#9a9694;
  --paper:#ffffff;
}
*{box-sizing:border-box;margin:0;padding:0}
html,body{width:1044px;height:1200px;overflow:hidden;background:#fff}
.canvas{position:relative;width:1044px;height:1200px;background:#fff;font-family:"Raleway",sans-serif;color:var(--ink)}
.slide{position:absolute;width:343px;height:192px;background:var(--paper);overflow:hidden;box-shadow:0 1px 3px rgba(0,0,0,.22)}
.c1{left:3px}.c2{left:351px}.c3{left:699px}
.r1{top:7px}.r2{top:206px}.r3{top:405px}.r4{top:604px}.r5{top:803px}.r6{top:1003px}
.abs{position:absolute}
.title{position:absolute;left:15px;top:14px;font:700 10.5px/1 "Montserrat",sans-serif;letter-spacing:.1px;color:var(--ink)}
.title::after{content:"";position:absolute;left:0;top:15px;width:16px;height:2px;background:var(--red)}
.brand{position:absolute;right:10px;top:12px;display:flex;flex-direction:column;align-items:center;gap:1px}
.brand .dot{width:9px;height:9px;border-radius:50%;border:1.3px solid var(--red)}
.brand span{font:700 3.8px/1 "Montserrat",sans-serif;color:var(--red);letter-spacing:.2px}
.foot{position:absolute;left:6px;bottom:5px;font:400 3.4px/1 "Raleway",sans-serif;color:#8d8987}
.page{position:absolute;right:6px;bottom:4px;width:8px;height:8px;border-radius:50%;background:var(--red);color:#fff;font:600 3px/8px "Montserrat",sans-serif;text-align:center}
.tiny{font:400 3.4px/1.45 "Raleway",sans-serif;color:var(--text)}
.tiny.w{color:#e9e7e6}
.h7{font:400 7px/1.2 "Raleway",sans-serif}
.photo{position:absolute}
.ph-desk{background:linear-gradient(135deg,#243444,#5f7a8f 55%,#c9d2d8)}
.ph-grey{background:linear-gradient(135deg,#cfcfcf,#8e8e8e 60%,#e4e4e4)}
.ph-hands{background:linear-gradient(160deg,#d9dde2,#7f8a95 50%,#b8bec4)}
.ph-dark{background:linear-gradient(120deg,#2a2a2a,#595655 45%,#161616)}
.ph-sunset{background:radial-gradient(circle at 55% 40%,#fff0b0,#f5a623 35%,#c05a10 75%,#6a2c08)}
.ph-sky{background:linear-gradient(180deg,#4a7fb8,#a9c8e3 55%,#e9eef2)}
.ph-runway{background:linear-gradient(180deg,#2f6fb3,#8fb8dc 45%,#f7c25a 60%,#3a4a5a)}
.ph-beach{background:linear-gradient(180deg,#5fa6e0,#c3e0f3 50%,#2f8fb8 62%,#d8c29a)}
.ph-wing{background:linear-gradient(160deg,#3a4450,#6d747a 55%,#2b2f33)}
.ph-city{background:linear-gradient(180deg,#f4f4f4,#dcdcdc)}
.ph-map{background:radial-gradient(ellipse at 50% 50%,#d2d2d2,#e6e6e6 70%,#fff)}
.ph-face{background:radial-gradient(circle at 50% 40%,#b8b2ad,#6f6a66)}
.tile{position:absolute;width:96px;height:56px;padding:9px 8px}
.tile h3{font:400 6.6px/1.2 "Raleway",sans-serif;color:#fff;margin-bottom:4px}
.box{position:absolute;width:66px;height:60px;padding:7px 6px;text-align:center}
.box h4{font:700 4.6px/1 "Montserrat",sans-serif;color:#fff;margin-bottom:2px}
.icon{position:absolute;border-radius:50%;display:flex;align-items:center;justify-content:center}
.label-red{font:400 4.6px/1 "Raleway",sans-serif;color:var(--red)}
.label{font:400 4.6px/1 "Raleway",sans-serif;color:#555}
.bar{position:absolute;bottom:57px;width:20px}
.bar span{position:absolute;top:-8px;left:0;width:100%;text-align:center;font:400 5px/1 "Montserrat",sans-serif;color:#333}
.pct{position:absolute;border-radius:50%;display:flex;align-items:center;justify-content:center;color:#fff;font:600 7px/1 "Montserrat",sans-serif}
.plan{position:absolute;background:#fff;text-align:center}
.plan .head{color:#fff;display:flex;flex-direction:column;justify-content:center;align-items:center}
.plan .price{font:400 11px/1 "Montserrat",sans-serif}
.plan .row{font:400 3.3px/1;color:#8d8987;border-bottom:.5px solid #e4e4e4;padding:4.5px 0}
table.data{position:absolute;left:24px;top:58px;width:296px;border-collapse:collapse;font:400 3.4px/1 "Raleway",sans-serif;color:#555}
table.data th{background:var(--ink);color:#fff;font-weight:600;height:8.5px}
table.data td{height:8.4px;text-align:center;border-bottom:.5px solid #fff}
table.data td:first-child{text-align:left;padding-left:16px}
table.data tr:nth-child(odd) td{background:#e2e1e1}
table.data tr:nth-child(even) td{background:#f1f0f0}
.member{position:absolute;display:flex;gap:5px}
.member .pic{width:27px;height:27px;border-radius:50%;flex:none}
.member b{display:block;font:400 6px/1.1 "Raleway",sans-serif;color:#222}
.member i{display:block;font:normal 400 3.4px/1.2 "Raleway",sans-serif;color:var(--red)}
.social{width:4px;height:4px;border-radius:50%;background:#222;display:inline-block;margin:0 .6px}
</style>
</head>
<body>
<div class="canvas">

  <!-- Row 1 -->
  <section class="slide c1 r1">
    <div class="title">YOUR TITLE GOES HERE</div>
    <div class="brand"><div class="dot"></div><span>LARKMOOR</span></div>
    <div class="tile photo ph-desk" style="left:24px;top:51px" role="img" aria-label="Person working at a desktop computer"></div>
    <div class="tile" style="left:122px;top:51px;background:var(--ink)"><h3>Heading Goes Here</h3><p class="tiny w">Lorem ipsum dolor sit amet consec adipiscing elit sed do eiusmod tempor incidunt ut labore et magna aliqua.</p></div>
    <div class="tile photo ph-grey" style="left:220px;top:51px" role="img" aria-label="Hands using a tablet at a desk"></div>
    <div class="tile" style="left:24px;top:110px;background:var(--red)"><h3>Heading Goes Here</h3><p class="tiny w">Lorem ipsum dolor sit amet consec adipiscing elit sed do eiusmod tempor incidunt ut labore et magna aliqua.</p></div>
    <div class="tile photo ph-hands" style="left:122px;top:110px" role="img" aria-label="Hands typing on a laptop"></div>
    <div class="tile" style="left:220px;top:110px;background:var(--stone)"><h3>Heading Goes Here</h3><p class="tiny w">Lorem ipsum dolor sit amet consec adipiscing elit sed do eiusmod tempor incidunt ut labore et magna aliqua.</p></div>
    <div class="foot">© Copyright 2017 Larkmoor Systems Division. All rights reserved</div>
    <div class="page">02</div>
  </section>

  <section class="slide c2 r1">
    <div class="photo ph-dark" style="left:0;top:0;width:240px;height:192px" role="img" aria-label="People working on a laptop in a dim office"></div>
    <div class="abs" style="left:172px;top:45px;width:171px;height:108px;background:rgba(30,30,30,.88);padding:18px 16px">
      <div class="h7" style="color:#fff;font-size:9.5px;position:relative">About Us<span style="position:absolute;left:0;top:13px;width:16px;height:1.5px;background:var(--red)"></span></div>
      <p class="tiny w" style="margin-top:11px">Lorem ipsum dolor sit amet, consectetur adipiscing elit, sed do eiusmod tempor incididunt ut labore et dolore magna aliqua.</p>
      <p class="tiny w" style="margin-top:5px">Ut enimad minim veniam, quis nostrud exercitation ullamco laboris nisi ut aliquip ex ea commodo consequat.</p>
    </div>
  </section>

  <section class="slide c3 r1">
    <div class="photo ph-wing" style="inset:0" role="img" aria-label="Aircraft wing above clouds at dusk"></div>
    <div class="brand" style="right:12px;top:12px"><div class="dot" style="width:14px;height:14px;border-color:#fff"></div><span style="font-size:6px">LARKMOOR</span></div>
    <div class="abs" style="left:20px;top:128px;font:600 15px/1 'Montserrat',sans-serif;color:#fff">THIS IS YOUR DIVIDER PAGE</div>
    <div class="abs" style="left:20px;top:150px;font:400 5px/1 'Raleway',sans-serif;color:#eee">Your Subtitle Goes Here</div>
  </section>

  <!-- Row 2 -->
  <section class="slide c1 r2">
    <div class="title">QUOTE AREA</div>
    <div class="brand"><div class="dot"></div><span>LARKMOOR</span></div>
    <div class="abs" style="left:0;top:43px;width:172px;height:118px;background:#222;padding:30px 14px 0 18px;color:#eee">
      <p style="font:300 7.3px/1.4 'Raleway',sans-serif">“ Coming together is a beginning.<br>Keeping together is progress.<br>Working together is success.”</p>
      <p style="font:300 8px/1 'Raleway',sans-serif;margin-top:9px">- Walter Brandt -</p>
    </div>
    <div class="photo ph-sunset" style="left:172px;top:43px;width:171px;height:118px" role="img" aria-label="Airplane flying through a golden sunset sky"></div>
    <div class="foot">© Copyright 2017 Larkmoor Systems Division. All rights reserved</div>
    <div class="page">05</div>
  </section>

  <section class="slide c2 r2">
    <div class="title">BRAND DETAILED</div>
    <div class="brand"><div class="dot"></div><span>LARKMOOR</span></div>
    <div class="photo ph-hands" style="left:22px;top:48px;width:160px;height:122px" role="img" aria-label="Laptop showing a website on a desk"></div>
    <div class="box" style="left:183px;top:48px;background:var(--ink)"><h4>System</h4><p class="tiny w">Mauris quam dolor, cursus at porta et, luctus eget purus. Nunc tempor luctus interdum.</p></div>
    <div class="box" style="left:251px;top:48px;background:var(--red)"><h4>Technology</h4><p class="tiny w">Mauris quam dolor, cursus at porta et, luctus eget purus. Nunc tempor luctus interdum.</p></div>
    <div class="box" style="left:183px;top:110px;background:var(--stone)"><h4>Leisure</h4><p class="tiny w">Mauris quam dolor, cursus at porta et, luctus eget purus. Nunc tempor luctus interdum.</p></div>
    <div class="box" style="left:251px;top:110px;background:#a9a5a3"><h4>Digital</h4><p class="tiny w">Mauris quam dolor, cursus at porta et, luctus eget purus. Nunc tempor luctus interdum.</p></div>
    <div class="foot">© Copyright 2017 Larkmoor Systems Division. All rights reserved</div>
    <div class="page">06</div>
  </section>

  <section class="slide c3 r2">
    <div class="title">PRODUCT PHILOSOPHY</div>
    <div class="brand"><div class="dot"></div><span>LARKMOOR</span></div>
    <svg class="abs" style="left:121px;top:55px" width="100" height="100" viewBox="0 0 100 100">
      <g transform="rotate(-90 50 50)" fill="none" stroke-width="17">
        <circle cx="50" cy="50" r="32" stroke="#e8222c" stroke-dasharray="30.2 171" stroke-dashoffset="0"/>
        <circle cx="50" cy="50" r="32" stroke="#807b78" stroke-dasharray="50.3 151" stroke-dashoffset="-30.2"/>
        <circle cx="50" cy="50" r="32" stroke="#c9c6c4" stroke-dasharray="40.2 161" stroke-dashoffset="-80.5"/>
        <circle cx="50" cy="50" r="32" stroke="#161616" stroke-dasharray="80.4 121" stroke-dashoffset="-120.7"/>
      </g>
      <circle cx="50" cy="50" r="14" fill="#fff" stroke="#ddd" stroke-width="1"/>
      <circle cx="50" cy="50" r="5" fill="none" stroke="#e8222c" stroke-width="1.3"/>
      <g font-family="Montserrat, sans-serif" font-size="5" fill="#fff">
        <text x="60" y="24">15%</text><text x="80" y="57">25%</text><text x="46" y="86">20%</text><text x="10" y="53">40%</text>
      </g>
    </svg>
    <div class="icon" style="left:106px;top:58px;width:22px;height:22px;background:var(--ink)"><svg width="11" height="11" viewBox="0 0 12 12"><circle cx="6" cy="6" r="5" fill="none" stroke="#fff" stroke-width="1"/><path d="M1 6h10M6 1c-3 3-3 7 0 10M6 1c3 3 3 7 0 10" stroke="#fff" stroke-width=".7" fill="none"/></svg></div>
    <div class="abs" style="left:20px;top:58px;width:82px;text-align:right"><div class="label">Secure</div><p class="tiny" style="margin-top:2px">Nullam eu tempor purus. Nunc a leo magna, sit amet consequat risus.</p></div>
    <div class="icon" style="left:106px;top:133px;width:22px;height:22px;background:#d6d4d3"><svg width="9" height="11" viewBox="0 0 9 11"><circle cx="4.5" cy="4" r="3.5" fill="none" stroke="#fff" stroke-width="1"/><path d="M3 9h3M3.5 10.5h2" stroke="#fff" stroke-width="1"/></svg></div>
    <div class="abs" style="left:20px;top:133px;width:82px;text-align:right"><div class="label" style="color:#aaa">Good Package</div><p class="tiny" style="margin-top:2px">Nullam eu tempor purus. Nunc a leo magna, sit amet consequat risus.</p></div>
    <div class="icon" style="left:227px;top:58px;width:22px;height:22px;background:var(--red)"><svg width="11" height="11" viewBox="0 0 12 12"><circle cx="3" cy="3" r="2" fill="none" stroke="#fff"/><circle cx="9" cy="9" r="2" fill="none" stroke="#fff"/><path d="M4.5 4.5l3 3" stroke="#fff"/></svg></div>
    <div class="abs" style="left:253px;top:58px;width:80px"><div class="label-red">Well Organized</div><p class="tiny" style="margin-top:2px">Nullam eu tempor purus. Nunc a leo magna, sit amet consequat risus.</p></div>
    <div class="icon" style="left:227px;top:133px;width:22px;height:22px;background:var(--stone)"><svg width="11" height="9" viewBox="0 0 12 10"><rect x=".5" y=".5" width="11" height="9" fill="none" stroke="#fff"/><path d="M2 3h8M2 5h5M2 7h6" stroke="#fff" stroke-width=".7"/></svg></div>
    <div class="abs" style="left:253px;top:133px;width:80px"><div class="label">Publication</div><p class="tiny" style="margin-top:2px">Nullam eu tempor purus. Nunc a leo magna, sit amet consequat risus.</p></div>
    <div class="foot">© Copyright 2017 Larkmoor Systems Division. All rights reserved</div>
    <div class="page">07</div>
  </section>

  <!-- Row 3 -->
  <section class="slide c1 r3">
    <div class="photo ph-city" style="inset:0" role="img" aria-label="Faint city skyline in light grey"></div>
    <div class="abs" style="left:160px;top:30px;font:400 3.4px/1 'Raleway',sans-serif;color:#555"><span style="color:var(--red)">■</span> 2014 &nbsp;■ 2015</div>
    <div class="bar" style="left:46px;height:60px;background:var(--red)"><span>400</span></div>
    <div class="bar" style="left:68px;height:75px;background:var(--ink)"><span>500</span></div>
    <div class="bar" style="left:116px;height:45px;background:var(--red)"><span>300</span></div>
    <div class="bar" style="left:138px;height:90px;background:var(--ink)"><span>600</span></div>
    <div class="bar" style="left:190px;height:43.5px;background:var(--red)"><span>290</span></div>
    <div class="bar" style="left:212px;height:30px;background:var(--ink)"><span>200</span></div>
    <div class="bar" style="left:265px;height:30px;background:var(--red)"><span>200</span></div>
    <div class="bar" style="left:288px;height:15px;background:var(--ink)"><span>100</span></div>
    <div class="abs" style="left:0;top:135px;width:343px;height:43px;background:var(--stone);display:flex;padding:11px 20px 0">
      <div style="flex:1;text-align:center"><b style="font:600 4.6px/1 'Montserrat',sans-serif;color:#fff">Asia</b><p class="tiny w">Duis quis purus adipiscing mi scelerisque dictum quis vel eros. Nullam eu tempor purus.</p></div>
      <div style="flex:1;text-align:center"><b style="font:600 4.6px/1 'Montserrat',sans-serif;color:#fff">Africa</b><p class="tiny w">Duis quis purus adipiscing mi scelerisque dictum quis vel eros. Nullam eu tempor purus.</p></div>
      <div style="flex:1;text-align:center"><b style="font:600 4.6px/1 'Montserrat',sans-serif;color:#fff">America</b><p class="tiny w">Duis quis purus adipiscing mi scelerisque dictum quis vel eros. Nullam eu tempor purus.</p></div>
      <div style="flex:1;text-align:center"><b style="font:600 4.6px/1 'Montserrat',sans-serif;color:#fff">Euro</b><p class="tiny w">Duis quis purus adipiscing mi scelerisque dictum quis vel eros. Nullam eu tempor purus.</p></div>
    </div>
  </section>

  <section class="slide c2 r3">
    <div class="title">TRENDING IN THE WORLD</div>
    <div class="brand"><div class="dot"></div><span>LARKMOOR</span></div>
    <div class="photo ph-map" style="left:12px;top:45px;width:222px;height:130px;border-radius:30px" role="img" aria-label="Grey world map"></div>
    <div class="pct" style="left:27px;top:91px;width:28px;height:28px;background:var(--red)">25%</div>
    <div class="pct" style="left:90px;top:80px;width:36px;height:36px;background:#4a4746;font-size:10px">80%</div>
    <div class="pct" style="left:186px;top:82px;width:36px;height:36px;background:#c3c0be;font-size:10px">75%</div>
    <div class="pct" style="left:155px;top:117px;width:22px;height:22px;background:#9e9a98;font-size:5.5px">15%</div>
    <div class="icon" style="left:241px;top:58px;width:24px;height:24px;border:1.2px solid var(--red)"><div style="width:7px;height:9px;background:var(--red);border-radius:1px"></div></div>
    <div class="abs" style="left:269px;top:58px;width:66px"><div class="label-red" style="font-size:4.4px">Confusion</div><p class="tiny">Nullam eu tempor purus. Nunc a leo magna, sit amet consequat risus.</p></div>
    <div class="icon" style="left:241px;top:94px;width:24px;height:24px;border:1.2px solid var(--ink)"><svg width="10" height="10" viewBox="0 0 10 10"><path d="M3 9V3M5 9V1.5M7 9V3M3 9h4" stroke="#161616" stroke-width="1.2" fill="none"/></svg></div>
    <div class="abs" style="left:269px;top:94px;width:66px"><div class="label" style="font-size:4.4px">Intangible</div><p class="tiny">Nullam eu tempor purus. Nunc a leo magna, sit amet consequat risus.</p></div>
    <div class="icon" style="left:241px;top:130px;width:24px;height:24px;border:1.2px solid #aaa"><svg width="10" height="10" viewBox="0 0 10 10"><path d="M2 9V6M4 9V4M6 9V2M8 9V5" stroke="#888" stroke-width="1.2"/></svg></div>
    <div class="abs" style="left:269px;top:130px;width:66px"><div class="label" style="font-size:4.4px">Performance</div><p class="tiny">Nullam eu tempor purus. Nunc a leo magna, sit amet consequat risus.</p></div>
    <div class="foot">© Copyright 2017 Larkmoor Systems Division. All rights reserved</div>
    <div class="page">08</div>
  </section>

  <section class="slide c3 r3">
    <div class="title">OUR VISION &amp; MISSION</div>
    <div class="brand"><div class="dot"></div><span>LARKMOOR</span></div>
    <div class="abs" style="left:0;top:44px;width:343px;height:122px;background:var(--ink)"></div>
    <div class="abs" style="left:16px;top:60px;width:150px;color:#fff">
      <div style="font:300 8px/1 'Raleway',sans-serif">• Our Vision:</div>
      <div style="font:600 6.4px/1.25 'Raleway',sans-serif;margin-top:6px">Go to the Next Level<br>Without look in the past</div>
      <p class="tiny w" style="margin-top:8px">Lorem ipsum dolor sit amet, consectetur adipiscing elit, sed do eiusmod tempor incididunt ut labore et dolore magna aliqua. Ut enimad minim veniam, quis nostrud exercitation ullamco laboris nisi ut aliquip ex ea commodo consequat.</p>
    </div>
    <div class="abs" style="left:190px;top:60px;font:300 8px/1 'Raleway',sans-serif;color:#fff">• Our Missions:</div>
    <div class="icon" style="left:198px;top:80px;width:12px;height:12px;background:#fff"><div style="width:5px;height:5px;background:var(--red);border-radius:1px"></div></div>
    <div class="abs" style="left:220px;top:78px;width:118px;color:#fff"><div style="font:400 7px/1 'Raleway',sans-serif">Your Text Here</div><p class="tiny w">Lorem ipsum dolor sit consectetur adipiscing elit, sed do eiusmod tempo.</p></div>
    <div class="icon" style="left:198px;top:106px;width:12px;height:12px;background:#fff"><div style="width:5px;height:5px;background:var(--red);border-radius:50%"></div></div>
    <div class="abs" style="left:220px;top:104px;width:118px;color:#fff"><div style="font:400 7px/1 'Raleway',sans-serif">Your Text Here</div><p class="tiny w">Lorem ipsum dolor sit consectetur adipiscing elit, sed do eiusmod tempo.</p></div>
    <div class="icon" style="left:198px;top:133px;width:12px;height:12px;background:#fff"><div style="width:5px;height:5px;background:var(--red);transform:rotate(45deg)"></div></div>
    <div class="abs" style="left:220px;top:131px;width:118px;color:#fff"><div style="font:400 7px/1 'Raleway',sans-serif">Your Text Here</div><p class="tiny w">Lorem ipsum dolor sit consectetur adipiscing elit, sed do eiusmod tempo.</p></div>
    <div class="foot">© Copyright 2017 Larkmoor Systems Division. All rights reserved</div>
    <div class="page">09</div>
  </section>

  <!-- Row 4 -->
  <section class="slide c1 r4">
    <div class="title">OUR SERVICES</div>
    <div class="brand"><div class="dot"></div><span>LARKMOOR</span></div>
    <div class="photo ph-sky" style="left:32px;top:42px;width:135px;height:84px" role="img" aria-label="Passenger jet flying above clouds"></div>
    <div class="abs" style="left:32px;top:131px;width:135px"><div class="label-red" style="font-size:5.6px">Your Title Goes Here</div><p class="tiny" style="margin-top:1px">Lorem ipsum dolor sit amet adipiscing elit, sed do eiusmod tempor incididunt ut labore et dolore magna aliqua. Ut enimad minim veniam, quis nostrud exercitation ullamco laboris nisi ut aliquip ex ea commodo consequat.</p></div>
    <div class="icon" style="left:188px;top:46px;width:13px;height:13px;background:var(--ink)"><svg width="6" height="6" viewBox="0 0 6 6"><path d="M1 5V3M3 5V1M5 5V2" stroke="#fff" stroke-width="1"/></svg></div>
    <div class="abs" style="left:211px;top:46px;width:120px"><div class="label" style="font-size:5.6px">Service Number One</div><p class="tiny">Lorem ipsum dolor sit amet, consectetur adipiscing elit, sed do eiusmod tempor incididunt ut labore et dolore magna aliqua.</p></div>
    <div class="icon" style="left:188px;top:87px;width:13px;height:13px;background:var(--red)"><div style="width:5px;height:5px;border:1px solid #fff;border-radius:50%"></div></div>
    <div class="abs" style="left:211px;top:87px;width:120px"><div class="label-red" style="font-size:5.6px">Service Number Two</div><p class="tiny">Lorem ipsum dolor sit amet, consectetur adipiscing elit, sed do eiusmod tempor incididunt ut labore et dolore magna aliqua.</p></div>
    <div class="icon" style="left:188px;top:128px;width:13px;height:13px;background:#9a9694"><svg width="6" height="6" viewBox="0 0 6 6"><circle cx="2.5" cy="2.5" r="1.7" fill="none" stroke="#fff" stroke-width=".8"/><path d="M3.8 3.8L5.5 5.5" stroke="#fff" stroke-width=".8"/></svg></div>
    <div class="abs" style="left:211px;top:128px;width:120px"><div class="label" style="font-size:5.6px">Service Number Three</div><p class="tiny">Lorem ipsum dolor sit amet, consectetur adipiscing elit, sed do eiusmod tempor incididunt ut labore et dolore magna aliqua.</p></div>
    <div class="foot">© Copyright 2017 Larkmoor Systems Division. All rights reserved</div>
    <div class="page">10</div>
  </section>

  <section class="slide c2 r4">
    <div class="title">THREE COLUMN DESCRIPTION</div>
    <div class="brand"><div class="dot"></div><span>LARKMOOR</span></div>
    <p class="abs" style="left:18px;top:46px;width:250px;font:400 6.6px/1.3 'Raleway',sans-serif;color:var(--red)">This is place for your header text. Insert your text here, just replace this text with your own text</p>
    <div class="abs" style="left:18px;top:76px;width:300px;display:flex;gap:10px">
      <div style="flex:1"><p class="tiny" style="font-size:3.9px">Lorem ipsum dolor sit amet, consectetur adipiscing elit, sed do eiusmod tempor incididunt ut labore et dolore magna aliqua. Ut enimad minim veniam, quis nostrud exercitation ullamco laboris nisi ut aliquip ex ea commodo consequat.</p><p class="tiny" style="font-size:3.9px;margin-top:5px">Duis aute irure dolor in reprehenderit in voluptate velit esse cillum dolore eu fugiat nulla pariatur excepteur.</p></div>
      <div style="flex:1;border-left:.5px solid #ddd;padding-left:6px"><p class="tiny" style="font-size:3.9px">Lorem ipsum dolor sit amet, consectetur adipiscing elit, sed do eiusmod tempor incididunt ut labore et dolore magna aliqua. Ut enimad minim veniam, quis nostrud exercitation ullamco laboris nisi ut aliquip ex ea commodo consequat.</p><p class="tiny" style="font-size:3.9px;margin-top:5px">Duis aute irure dolor in reprehenderit in voluptate velit esse cillum dolore eu fugiat nulla pariatur excepteur.</p></div>
      <div style="flex:1;border-left:.5px solid #ddd;padding-left:6px"><p class="tiny" style="font-size:3.9px">Lorem ipsum dolor sit amet, consectetur adipiscing elit, sed do eiusmod tempor incididunt ut labore et dolore magna aliqua. Ut enimad minim veniam, quis nostrud exercitation ullamco laboris nisi ut aliquip ex ea commodo consequat.</p><p class="tiny" style="font-size:3.9px;margin-top:5px">Duis aute irure dolor in reprehenderit in voluptate velit esse cillum dolore eu fugiat nulla pariatur excepteur.</p></div>
    </div>
    <div class="foot">© Copyright 2017 Larkmoor Systems Division. All rights reserved</div>
    <div class="page">11</div>
  </section>

  <section class="slide c3 r4">
    <div class="title">OUR TEAM</div>
    <div class="brand"><div class="dot"></div><span>LARKMOOR</span></div>
    <div class="photo ph-face" style="left:131px;top:35px;width:81px;height:81px;border-radius:50%" role="img" aria-label="Portrait of the CEO"></div>
    <div class="abs" style="left:96px;top:124px;width:151px;text-align:center">
      <div style="font:400 3.8px/1 'Raleway',sans-serif;color:#555">Mr. John Smith</div>
      <div style="font:400 3.8px/1.3 'Raleway',sans-serif;color:var(--red)">CEO</div>
      <p class="tiny">Lorem ipsum dolor sit amet, consectetur adipiscing elit, sed do eiusmod tempor incididunt ut labore et dolore magna aliqua. Ut enimad minim veniam, quis nostrud exercitation ullamco laboris nisi ut aliquip.</p>
      <div style="margin-top:3px"><span class="social"></span><span class="social"></span><span class="social"></span><span class="social"></span></div>
    </div>
    <div class="foot">© Copyright 2017 Larkmoor Systems Division. All rights reserved</div>
    <div class="page">12</div>
  </section>

  <!-- Row 5 -->
  <section class="slide c1 r5">
    <div class="title">MONTHLY SUBSCRIPTION</div>
    <div class="brand"><div class="dot"></div><span>LARKMOOR</span></div>
    <div class="abs" style="left:0;top:93px;width:343px;height:99px;background:var(--ink)"></div>
    <div class="plan" style="left:50px;top:64px;width:70px;height:88px">
      <div class="head" style="height:29px;background:var(--stone)"><span class="price">$300</span><span class="tiny w" style="font-size:3px">per month</span></div>
      <div class="row tiny">Single Edition</div><div class="row tiny">30gb Cloud Service</div><div class="row tiny">3 User</div><div class="row tiny" style="border:0">Free Update</div>
    </div>
    <div class="plan" style="left:127px;top:60px;width:89px;height:102px">
      <div class="head" style="height:33px;background:var(--red)"><span class="price" style="font-size:14px">$900</span><span class="tiny w" style="font-size:3px">per month</span></div>
      <div class="row tiny" style="padding:5.5px 0">Business Edition</div><div class="row tiny" style="padding:5.5px 0">80gb Cloud Service</div><div class="row tiny" style="padding:5.5px 0">6 User</div><div class="row tiny" style="border:0;padding:5.5px 0">Free Update</div>
    </div>
    <div class="plan" style="left:223px;top:64px;width:70px;height:88px">
      <div class="head" style="height:29px;background:var(--stone)"><span class="price">$400</span><span class="tiny w" style="font-size:3px">per month</span></div>
      <div class="row tiny">Single Edition</div><div class="row tiny">30gb Cloud Service</div><div class="row tiny">3 User</div><div class="row tiny" style="border:0">Free Update</div>
    </div>
  </section>

  <section class="slide c2 r5">
    <div class="title">YOUR TITLE GOES HERE</div>
    <div class="brand"><div class="dot"></div><span>LARKMOOR</span></div>
    <p class="abs tiny" style="left:26px;top:43px;width:190px;font-size:2.8px"><span style="color:var(--red)">Description</span> : This are most common of sample text used to fill the layout of the table data rows in this slide.</p>
    <table class="data">
      <tr><th></th><th>Value</th><th>Value</th><th>Value</th><th>Value</th></tr>
      <tr><td>Lorem ipsumc</td><td>10</td><td>15</td><td>16</td><td>18</td></tr>
      <tr><td>Lorem ipsumc</td><td>12</td><td>13</td><td>15</td><td>16</td></tr>
      <tr><td>Lorem ipsumc</td><td>20</td><td>22</td><td>21</td><td>21</td></tr>
      <tr><td>Lorem ipsumc</td><td>10</td><td>21</td><td>12</td><td>21</td></tr>
      <tr><td>Lorem ipsumc</td><td>25</td><td>25</td><td>25</td><td>25</td></tr>
      <tr><td>Lorem ipsumc</td><td>10</td><td>02</td><td>51</td><td>21</td></tr>
      <tr><td>Lorem ipsumc</td><td>35</td><td>35</td><td>65</td><td>32</td></tr>
      <tr><td>Lorem ipsumc</td><td>26</td><td>33</td><td>35</td><td>32</td></tr>
      <tr><td>Lorem ipsumc</td><td>32</td><td>10</td><td>32</td><td>32</td></tr>
    </table>
    <div class="foot">© Copyright 2017 Larkmoor Systems Division. All rights reserved</div>
    <div class="page">14</div>
  </section>

  <section class="slide c3 r5">
    <div class="title">OUR TEAM</div>
    <div class="brand"><div class="dot"></div><span>LARKMOOR</span></div>
    <div class="member" style="left:20px;top:46px;width:140px"><div class="pic ph-face" role="img" aria-label="Portrait of Michael Doe"></div><div><b>Michael Doe</b><i>CEO</i><p class="tiny">MSHRTI, MBA and CIMA Dip PM</p><p class="tiny">• Lorem ipsum dolor sit amet, consectetur adipiscing elit<br>• sed do eiusmod tempor incididunt ut labore et dolore magna<br>• Ut enimad minim veniam, quis nostrud exercitation</p></div></div>
    <div class="member" style="left:174px;top:46px;width:150px"><div class="pic ph-face" role="img" aria-label="Portrait of James Doe"></div><div><b>James Doe</b><i>Manager</i><p class="tiny">M.B.A</p><p class="tiny">• Lorem ipsum dolor sit amet, consectetur adipiscing elit<br>• sed do eiusmod tempor incididunt ut labore et dolore magna<br>• Ut enimad minim veniam, quis nostrud exercitation</p></div></div>
    <div class="member" style="left:20px;top:111px;width:140px"><div class="pic ph-face" role="img" aria-label="Portrait of Jane Doe"></div><div><b>Jane Doe</b><i>Doctor of Chemistry</i><p class="tiny">M.B.A</p><p class="tiny">• Lorem ipsum dolor sit amet, consectetur adipiscing elit<br>• sed do eiusmod tempor incididunt ut labore et dolore magna<br>• Ut enimad minim veniam, quis nostrud exercitation</p></div></div>
    <div class="member" style="left:174px;top:111px;width:150px"><div class="pic ph-face" role="img" aria-label="Portrait of John Doe"></div><div><b>John Doe</b><i>Doctor of Physical</i><p class="tiny">Professor</p><p class="tiny">• Lorem ipsum dolor sit amet, consectetur adipiscing elit<br>• sed do eiusmod tempor incididunt ut labore et dolore magna<br>• Ut enimad minim veniam, quis nostrud exercitation</p></div></div>
    <div class="foot">© Copyright 2017 Larkmoor Systems Division. All rights reserved</div>
    <div class="page">15</div>
  </section>

  <!-- Row 6 -->
  <section class="slide c1 r6">
    <div class="title">CUSTOMER TESTIMONIALS</div>
    <div class="brand"><div class="dot"></div><span>LARKMOOR</span></div>
    <div class="photo ph-face" style="left:74px;top:42px;width:47px;height:47px;border-radius:50%" role="img" aria-label="Portrait of a customer"></div>
    <p class="abs tiny" style="left:147px;top:48px;width:160px;font-size:3.8px">adipiscing elit, sed diam nonummy nibh euismod tincidunt ut laoreet dolore magna aliquam erat volutpat. Ut wisi enim <span style="color:#333">Lorem ipsum</span> dolor sit amet, consectetur adipiscing elit, sed diam nonummy nibh euismod tincidunt ut laoreet dolore magna.</p>
    <div class="abs" style="left:0;top:138px;width:343px;height:54px;background:var(--ink)"></div>
    <div class="abs" style="left:93px;top:134px;width:0;height:0;border-left:4px solid transparent;border-right:4px solid transparent;border-bottom:4px solid var(--ink)"></div>
    <div class="abs" style="left:0;top:144px;width:343px;display:flex;justify-content:space-around;padding:0 44px">
      <div style="width:60px;text-align:center"><div class="icon" style="position:relative;margin:0 auto;width:24px;height:24px;border:1px solid #fff"><div style="width:9px;height:7px;border:1px solid #fff"></div></div><p class="tiny w" style="margin-top:5px;font-size:3px">Why does getting a loan have to be so much more complicated than ordering a fridge on Northcart?</p></div>
      <div style="width:60px;text-align:center"><div class="icon" style="position:relative;margin:0 auto;width:24px;height:24px;border:1px solid #fff"><div style="width:9px;height:7px;border:1px solid #fff;border-radius:1px"></div></div><p class="tiny w" style="margin-top:5px;font-size:3px">Why do I have to go to a branch, fill out forms and wait for weeks to get a response?</p></div>
      <div style="width:60px;text-align:center"><div class="icon" style="position:relative;margin:0 auto;width:24px;height:24px;border:1px solid #fff"><div style="width:8px;height:8px;border:1px solid #fff"></div></div><p class="tiny w" style="margin-top:5px;font-size:3px">Why do banks refuse to lend to me despite the substantial fees I receive each month?</p></div>
      <div style="width:60px;text-align:center"><div class="icon" style="position:relative;margin:0 auto;width:24px;height:24px;border:1px solid #fff"><div style="width:9px;height:7px;border:1px solid #fff;border-top-width:2px"></div></div><p class="tiny w" style="margin-top:5px;font-size:3px">Why is there no Northcart in banking, that identifies my needs and offers convenience at fair prices?</p></div>
    </div>
  </section>

  <section class="slide c2 r6">
    <div class="title">TWO PICTURES SLIDE</div>
    <div class="brand"><div class="dot"></div><span>LARKMOOR</span></div>
    <div class="photo ph-runway" style="left:26px;top:42px;width:144px;height:133px" role="img" aria-label="Airplane tail on a runway at sunrise"></div>
    <div class="photo ph-sunset" style="left:174px;top:42px;width:143px;height:133px" role="img" aria-label="Airplane flying through golden clouds"></div>
    <div class="foot">© Copyright 2017 Larkmoor Systems Division. All rights reserved</div>
    <div class="page">17</div>
  </section>

  <section class="slide c3 r6">
    <div class="title">TITLE AND IMAGE + TEXT</div>
    <div class="brand"><div class="dot"></div><span>LARKMOOR</span></div>
    <div class="photo ph-beach" style="left:24px;top:42px;width:296px;height:71px" role="img" aria-label="Friends jumping on a sunny beach"></div>
    <p class="abs" style="left:26px;top:118px;width:140px;font:400 6px/1.25 'Raleway',sans-serif;color:var(--red)">Lorem ipsum dolor sit amet, consectetur adipiscing elit, sed do eiusmod tempor incididunt ut labore et dolore magna aliqua. Ut enimad minim veniam, quis Lorem ipsum dolor sit amet</p>
    <div class="abs" style="left:174px;top:118px;width:146px"><p class="tiny" style="font-size:3.8px">Lorem ipsum dolor sit amet, consectetur adipiscing elit, sed do eiusmod tempor incididunt ut labore et dolore magna aliqua. Ut enimad minim veniam, quis nostrud exercitation ullamco laboris nisi ut aliquip ex ea commodo consequat.</p><p class="tiny" style="font-size:3.8px;margin-top:4px">Duis aute irure dolor in reprehenderit in voluptate velit esse cillum dolore eu fugiat nulla pariatur. Excepteur sint occaecat cupidatat non proident, sunt in culpa qui officia deserunt mollit anim id est laborum.</p></div>
    <div class="foot">© Copyright 2017 Larkmoor Systems Division. All rights reserved</div>
    <div class="page">18</div>
  </section>

</div>
</body>
</html>
```